e-Book Cover Design Project

I need an e-book cover design for a book called The Quiet Harbor. A fieldbook for hearts (run dry). It is non-fiction. It has an apple theme throughout so I would like to see designs that use a red apple (perhaps even a bite out of it), simple text and simple background. Despite the theme, the final design should still be positive.

Target Market(s)

Most likely women aged 25 and over.

Requirements
Must have
• real red apple
Nice to have
• cupids arrow
Should not have
• cartoons

```html
<!DOCTYPE html>
<html lang="en">
<head>
<meta charset="utf-8">
<title>The Quiet Harbor — eBook Cover</title>
<link rel="stylesheet" href="https://fonts.googleapis.com/css2?family=Questrial&display=swap">
<style>
  :root {
    --ink: #2b1a14;
    --accent-red: #c81b1e;
    --bg-top: #ffffff;
    --bg-bottom: #cfcfcf;
    --frame: #3a3a3a;
    --apple-light: #e23a2c;
    --apple-mid: #c41a1c;
    --apple-dark: #9a1014;
    --leaf-green: #3aa52a;
    --author: #1f1f1f;
  }
  html, body {
    margin: 0;
    padding: 0;
    overflow: hidden;
    background: #ffffff;
  }
  .cover {
    position: relative;
    width: 750px;
    height: 1200px;
    box-sizing: border-box;
    border: 1px solid var(--frame);
    background: linear-gradient(to bottom, var(--bg-top) 0%, var(--bg-top) 30%, var(--bg-bottom) 100%);
    overflow: hidden;
    font-family: "Questrial", sans-serif;
  }
  .title {
    margin: 0;
    font-weight: 400;
  }
  .title-line-one {
    position: absolute;
    left: 98px;
    top: 34px;
    font-size: 140px;
    line-height: 1;
    letter-spacing: -1px;
    color: var(--ink);
    white-space: nowrap;
  }
  .title-line-two {
    position: absolute;
    left: 96px;
    top: 118px;
    font-size: 160px;
    line-height: 1;
    letter-spacing: -2px;
    color: var(--accent-red);
    white-space: nowrap;
  }
  .title-initial {
    font-size: 232px;
    line-height: 1;
    margin-right: -6px;
  }
  .cover-art {
    position: absolute;
    left: 118px;
    top: 205px;
    width: 508px;
    height: 860px;
    border-radius: 40px;
    background:
      radial-gradient(ellipse 30% 16% at 42% 42%, rgba(58, 165, 42, 0.55), rgba(58, 165, 42, 0) 100%),
      radial-gradient(ellipse 50% 32% at 50% 66%, var(--apple-light) 0%, var(--apple-mid) 60%, var(--apple-dark) 85%, rgba(154, 16, 20, 0) 100%);
  }
  .author {
    position: absolute;
    left: 0;
    right: 0;
    top: 1108px;
    margin: 0;
    text-align: center;
    font-size: 46px;
    font-weight: 400;
    color: var(--author);
  }
</style>
</head>
<body>
  <main class="cover">
    <h1 class="title">
      <span class="title-line-one">The Quiet</span>
      <span class="title-line-two"><span class="title-initial">H</span>arbor</span>
    </h1>

    <div class="cover-art" role="img" aria-label="Photograph of a glossy red apple with a green leaf at its stem, a heart shape carved into its skin, and a cupid's arrow with black fletching standing in its top"></div>

    <p class="author">Maren Whitfield</p>
  </main>
</body>
</html>
```